California, rapidly growing Insurance Agency needs logo and letterhead design

we need a logo design and letterhead for an insurance company that specialize in providing businesses with insurance (workers comp , group health insurance, business insurance). I would like to see designs with a professional layout that use dark rich blues, and maybe some lighter blues mixed in. Also open to using grey and red tones. The design should communicate professional, yet current day feel (not too old/stuff or boring feel).
Updates

The company name is “Dovrel Insurance Services” If possible , would like to see a letterhead option with tag line worked in somewhere as “insurance specialist for over 45 years” Thank you!!!!

Target Market(s)

We insure businesses, do would like professional look with out being too stuffy or boring

Industry/Entity Type

Insurance Agency

Logo Text

Maybe “We make Insurance easy”

Font styles to use
Serif

Colors
3176b5
0993cd
f04b51

Requirements
Nice to have
• Would like to have rich dark blues and light mixed or also open to grey and
• Red color scheme
Should not have
• We target higher end clients, so would like to stay away from
• Any type of anime graphic

```html
<!DOCTYPE html>
<html lang="en">
<head>
<meta charset="utf-8">
<title>Dovrel Insurance Services — Letterhead</title>
<link rel="stylesheet" href="https://fonts.googleapis.com/css2?family=Roboto:wght@400;700&display=swap">
<style>
  :root {
    --backdrop: #e6e6ea;
    --paper: #fafafa;
    --ink-dark: #3c3f47;
    --ink-body: #4a4d55;
    --rule-grey: #8a8c92;
    --brand-blue: #1a5cc0;
  }
  * { margin: 0; padding: 0; box-sizing: border-box; }
  html, body {
    width: 1200px;
    height: 1161px;
    overflow: hidden;
    background: var(--backdrop);
    font-family: "Roboto", Arial, sans-serif;
  }
  .letterhead {
    position: absolute;
    left: 180px;
    top: 37px;
    width: 840px;
    height: 1087px;
    background: var(--paper);
  }
  .brand {
    position: absolute;
    left: 69px;
    top: 76px;
    display: flex;
    align-items: center;
    gap: 10px;
  }
  .brand-mark {
    width: 16px;
    height: 16px;
    background: var(--brand-blue);
  }
  .brand-name {
    font-size: 26px;
    font-weight: 700;
    color: var(--ink-dark);
    letter-spacing: -0.2px;
  }
  .footer-rule {
    position: absolute;
    left: 70px;
    top: 1000px;
    width: 701px;
    height: 1px;
    background: var(--rule-grey);
  }
  .footer-accent {
    position: absolute;
    left: 627px;
    top: 998px;
    width: 144px;
    height: 3px;
    background: var(--brand-blue);
  }
  .contact {
    position: absolute;
    left: 70px;
    top: 1015px;
    font-size: 10.5px;
    line-height: 13px;
    color: var(--ink-body);
  }
  .tagline {
    position: absolute;
    right: 69px;
    top: 1014px;
    text-align: right;
    font-size: 10.5px;
    line-height: 13px;
    font-weight: 700;
    color: var(--ink-dark);
    text-transform: uppercase;
  }
</style>
</head>
<body>
  <main class="letterhead">
    <header class="brand">
      <span class="brand-mark"></span>
      <span class="brand-name">Dovrel Insurance Services</span>
    </header>

    <footer>
      <div class="footer-rule"></div>
      <div class="footer-accent"></div>
      <address class="contact" style="font-style: normal;">
        2280 Harbor View Avenue, Seal Point, CA 90412<br>
        Phone: 555.214.3370 · Fax: 555.214.3371
      </address>
      <p class="tagline">Insurance specialist<br>for over 45 years</p>
    </footer>
  </main>
</body>
</html>
```